" A Empresa se chama Vento Sul Hotéis. Somos uma empresa do ramo hoteleiro. Esta é a marca da Holding que participa em todos os empreendimentos que administramos. Somos novos no mercado hoteleiro mas temos mais de 30 anos de tradiçao no mercado de construçao e imóveis. "

```html
<!DOCTYPE html>
<html lang="pt-BR">
<head>
<meta charset="utf-8">
<title>Vento Sul Hotéis – Envelope Saco</title>
<link href="https://fonts.googleapis.com/css2?family=Montserrat:wght@400;500&display=swap" rel="stylesheet">
<style>
  :root {
    --backdrop: #e6e4e1;
    --paper: #ffffff;
    --brand-orange: #f0792f;
    --brand-grey: #6b6b6b;
    --fine-grey: #8a8a8a;
  }
  html, body {
    margin: 0;
    width: 1200px;
    height: 1200px;
    overflow: hidden;
    background: var(--backdrop);
    font-family: "Montserrat", Arial, sans-serif;
  }
  .canvas { position: relative; width: 1200px; height: 1200px; }
  .envelope-shape { position: absolute; inset: 0; }
  .brand {
    position: absolute;
    display: flex;
    align-items: center;
    gap: 10px;
    color: var(--brand-grey);
    font-weight: 500;
    letter-spacing: 0.04em;
    white-space: nowrap;
  }
  .brand-mark { background: var(--brand-orange); }
  .brand--header { left: 258px; top: 322px; font-size: 26px; }
  .brand--header .brand-mark { width: 22px; height: 22px; }
  .brand--footer { left: 792px; top: 912px; font-size: 22px; }
  .brand--footer .brand-mark { width: 18px; height: 18px; }
  .sender-details {
    position: absolute;
    left: 720px;
    width: 300px;
    top: 950px;
    text-align: center;
    color: var(--fine-grey);
    font-size: 9px;
    line-height: 15px;
    font-weight: 400;
  }
  .sender-details p { margin: 0; }
</style>
</head>
<body>
<main class="canvas">
  <svg class="envelope-shape" width="1200" height="1200" viewBox="0 0 1200 1200" aria-hidden="true">
    <path class="envelope-tab" d="M100,270 L104,222 Q106,204 126,204 L578,204 Q598,204 600,222 L604,270 Z" fill="var(--brand-orange)"/>
    <path class="envelope-body" d="M60,250 L604,250 Q616,250 622,266 L630,286 Q636,300 652,300 L1098,300 Q1116,300 1116,318 L1116,1056 L372,1056 L355,1090 L100,1090 L60,975 Z" fill="var(--paper)"/>
    <line class="footer-rule" x1="607" y1="953" x2="703" y2="953" stroke="var(--brand-orange)" stroke-width="4"/>
    <line class="footer-rule" x1="1020" y1="953" x2="1116" y2="953" stroke="var(--brand-orange)" stroke-width="4"/>
  </svg>

  <div class="brand brand--header">
    <span class="brand-mark"></span>
    <span class="brand-name">Vento Sul Hotéis</span>
  </div>

  <div class="brand brand--footer">
    <span class="brand-mark"></span>
    <span class="brand-name">Vento Sul Hotéis</span>
  </div>

  <div class="sender-details">
    <p class="sender-address">Rua das Gaivotas 120, Sala 8 · Porto Alegre · RS</p>
    <p class="sender-web">www.ventosulhoteis.com.br</p>
  </div>
</main>
</body>
</html>
```